Martin Halvorsen Pianist Teacher Examiner

I need a website design to promote my business as a professional classical pianist and a piano teacher of all levels.
I want it to look a mixture of old world opulence (eg antique grand piano?) and modern text. It should have an elegant, beautiful and relaxing feel.

Industry/Entity Type

Teacher

```html
<!DOCTYPE html>
<html lang="en">
<head>
<meta charset="utf-8">
<title>Martin Halvorsen — Pianist, Teacher, Examiner</title>
<link href="https://fonts.googleapis.com/css2?family=Gelasio:wght@400&family=Kristi&display=swap" rel="stylesheet">
<style>
  :root {
    --page-bg: #ddd6a4;
    --page-bg-light: #e6e0b4;
    --panel: #f2efd3;
    --heading: #3c3a30;
    --body-text: #7d7862;
    --nav-text: #5a574a;
    --footer-bg: #c8c072;
    --white: #ffffff;
    --icon-dark: #111111;
  }
  * { margin: 0; padding: 0; box-sizing: border-box; }
  html, body { width: 1142px; height: 1200px; overflow: hidden; }
  body {
    position: relative;
    background: radial-gradient(ellipse at 50% 40%, var(--page-bg-light), var(--page-bg));
    font-family: "Gelasio", Georgia, serif;
    color: var(--body-text);
  }
  .site-logo {
    position: absolute; left: 152px; top: 58px;
    font-size: 38px; color: var(--white); letter-spacing: 0.5px;
  }
  .social {
    position: absolute; left: 708px; top: 28px; display: flex; gap: 4px;
  }
  .social span { width: 28px; height: 28px; border-radius: 50%; background: var(--icon-dark); display: block; }
  .search {
    position: absolute; left: 806px; top: 32px; width: 184px; height: 22px;
    background: var(--white); border: 1px solid #cfcab0;
    font-size: 9px; color: #b5b3a6; padding: 5px 6px;
  }
  .search svg { position: absolute; right: 6px; top: 5px; }
  .main-nav {
    position: absolute; right: 152px; top: 84px; display: flex; gap: 19px;
    font-size: 15.5px; color: var(--nav-text);
  }
  .main-nav a { color: inherit; text-decoration: none; }
  .hero {
    position: absolute; left: 148px; top: 120px; width: 845px; height: 439px;
    background: linear-gradient(90deg, #2e2e30 0%, #232325 55%, #4a4a4e 72%, #3a3a3d 100%);
  }
  .hero-title {
    position: absolute; left: 0; right: 0; top: 208px; text-align: center;
    font-size: 40px; color: #a9a9a9; padding-left: 115px;
  }
  .hero-tagline {
    position: absolute; left: 0; right: 0; top: 258px; text-align: center;
    font-family: "Kristi", cursive; font-size: 30px; color: var(--white); padding-left: 115px;
  }
  .hero-dots { position: absolute; top: 402px; left: 389px; display: flex; gap: 9px; }
  .hero-dots span { width: 17px; height: 17px; border-radius: 50%; background: var(--white); }
  .hero-dots span.active { background: #555; }
  .feature-photo {
    position: absolute; left: 148px; top: 600px; width: 238px; height: 459px;
    background: linear-gradient(180deg, #8a6a3a 0%, #c8a96a 35%, #6d5436 70%, #3b2a1e 100%);
  }
  .panel { position: absolute; top: 600px; height: 459px; background: var(--panel); overflow: hidden; }
  .panel-welcome { left: 386px; width: 326px; padding: 30px 8px 0 14px; }
  .panel-about { left: 720px; width: 273px; padding: 30px 8px 0 14px; }
  .panel h2 { font-weight: 400; font-size: 21px; color: var(--heading); margin-bottom: 10px; white-space: nowrap; }
  .panel-about h2 { font-size: 20px; padding-left: 8px; margin-bottom: 14px; }
  .panel p { font-size: 11.6px; line-height: 19.3px; }
  .portrait {
    width: 148px; height: 146px; margin: 0 0 16px 62px;
    background: linear-gradient(160deg, #6e6e70, #3c3c3e 60%, #1e1e20);
  }
  .site-footer {
    position: absolute; left: 0; top: 1118px; width: 1142px; height: 82px;
    background: var(--footer-bg); color: var(--white); text-align: center;
  }
  .footer-nav { margin-top: 17px; font-size: 12.5px; }
  .footer-nav a { color: inherit; text-decoration: none; }
  .footer-nav .sep { margin: 0 12px; }
  .copyright { margin-top: 19px; font-size: 12.5px; }
</style>
</head>
<body>
  <header>
    <div class="site-logo">martinhalvorsen.com</div>
    <div class="social" aria-label="Social links"><span></span><span></span><span></span></div>
    <div class="search">Search
      <svg width="10" height="10" viewBox="0 0 10 10"><circle cx="4" cy="4" r="3" fill="none" stroke="#aaa" stroke-width="1.3"/><line x1="6.2" y1="6.2" x2="9.5" y2="9.5" stroke="#aaa" stroke-width="1.5"/></svg>
    </div>
    <nav class="main-nav">
      <a href="#">Home</a><a href="#">About Me</a><a href="#">Classes</a><a href="#">Testimonials</a><a href="#">Contact Us</a>
    </nav>
  </header>

  <section class="hero" role="img" aria-label="Portraits of the pianist in a leather jacket beside a white piano, on a dark studio backdrop">
    <div class="hero-title">Martin Halvorsen</div>
    <div class="hero-tagline">With My Instrument</div>
    <div class="hero-dots"><span class="active"></span><span></span><span></span></div>
  </section>

  <div class="feature-photo" role="img" aria-label="Black grand piano in an ornate gilded antique salon"></div>

  <section class="panel panel-welcome">
    <h2>Welcome to Martin Halvorsen</h2>
    <p>Lorem Ipsum is simply dummy text of the printing and typesetting industry. Lorem Ipsum has been the industry's standard dummy text ever since the 1500s, when an unknown printer took a galley of type and scrambled it to make a type specimen book. It has survived not only five centuries, but also the leap into electronic typesetting, remaining essentially unchanged. It was popularised in the 1960s with the release of Typeleaf sheets containing Lorem Ipsum passages, and more recently with desktop publishing software like Quillset Composer including versions of Lorem Ipsum.Lorem Ipsum is simply dummy text of the printing and typesetting industry. Lorem Ipsum has been the industry's standard dummy text ever since the 1500s, when an unknown printer took a galley of type and scrambled it to make a type specimen book. It has survived not only five centuries, but also the leap into electronic typesetting, remaining essentially unchanged. It was popularised in the 1960s with the release of Typeleaf sheets containing &nbsp;.</p>
  </section>

  <section class="panel panel-about">
    <h2>About Martin Halvorsen</h2>
    <div class="portrait" role="img" aria-label="Head-and-shoulders portrait of the pianist"></div>
    <p>Lorem Ipsum is simply dummy text of the printing and typesetting industry. Lorem Ipsum has been the industry's standard dummy text ever since the 1500s, when an unknown printer took a galley of type and scrambled it to make a type specimen book. It has survived not only five centuries, but also the leap into electronic typesetting, remaining essentially unchanged. It was popularised in the 1960s with the release of Typeleaf sheets containing</p>
  </section>

  <footer class="site-footer">
    <nav class="footer-nav">
      <a href="#">Home</a><span class="sep">|</span><a href="#">About Me</a><span class="sep">|</span><a href="#">Classes</a><span class="sep">|</span><a href="#">Testimonials</a><span class="sep">|</span><a href="#">Contact Us</a>
    </nav>
    <div class="copyright">© 2014 Company &nbsp;Name,All Rights reserved</div>
  </footer>
</body>
</html>
```